Flyer für Installationsfirma für hochwertige Multimedia- und Beschallungslösungen, insbesonder in Kirchen und öffentlichen Bereichen mit Menschenansammlungen
Zielgruppe
Wir sind eine Installationsfirma für hochwertige Multimedia- und Beschallungslösungen in akustisch schwierigen Räumen. Im weiteren auch der Umbau auf LED Leuchten und dazugehörende Steuerungen. Unser Geschäft ist in Festinstallationen und Rentalbereich 'unterteilt' Weitere Infos auch auf www. alpen-ton.ch
Unser Zielpublikum sind die Festinstallation für Kirchen und öffentliche Räume. Mehrzweckräume, Bühnen, Kirchen, Aulas, Bahnhofshallen, Warteräume, Konferenzräume, Tagungszentren usw. Bei diesem Flyer sollen speziell die Kirchen beworben werden. Es ist wichtig dass nebst den oben beschriebenen Leistungen auch die Displaylösung für Liedanzeigen hervorgehoben wird.
Aufgabenstellung
Ansprechender Werbe-Flyer A4 2 Seitig
Spezifische Bilder und Texte zu den versch. Angebotsbereichen für Kirchen im Anhang. Vorschläge des Grafikers sind willkommen !
Die Texte und Bilder sollten von uns angepasst und korrigiert werden können !

```html
<!DOCTYPE html>
<html lang="de">
<head>
<meta charset="utf-8">
<title>Alpenton – Flyer Kirchen</title>
<link rel="stylesheet" href="https://fonts.googleapis.com/css2?family=Poppins:wght@400;500;600;800&display=swap">
<style>
  :root {
    --page-bg: #ececec;
    --navy-top: #2a3344;
    --navy-mid: #1b2638;
    --navy-deep: #111827;
    --navy-footer: #0f2b4a;
    --accent-blue: #2fb1e4;
    --white: #ffffff;
    --text-soft: #e6ecf4;
    --warm-dark: #3a2416;
    --warm-light: #b06a2c;
  }
  * { box-sizing: border-box; margin: 0; padding: 0; }
  html, body {
    width: 1200px; height: 800px; overflow: hidden;
    background: var(--page-bg);
    font-family: "Poppins", sans-serif;
  }
  .flyer {
    position: absolute; left: 330px; top: 18px;
    width: 540px; height: 764px;
    background: linear-gradient(160deg, var(--navy-top) 0%, var(--navy-mid) 45%, var(--navy-deep) 100%);
    overflow: hidden;
    box-shadow: 0 10px 30px rgba(0,0,0,0.25);
  }
  .hero-photo {
    position: absolute; left: 0; top: 0; width: 540px; height: 400px;
    background:
      radial-gradient(ellipse at 50% 40%, var(--warm-light) 0%, var(--warm-dark) 45%, #1d1a1c 85%);
    -webkit-mask-image: linear-gradient(180deg, #000 40%, transparent 100%);
    mask-image: linear-gradient(180deg, #000 40%, transparent 100%);
  }
  .headline {
    position: absolute; left: 38px; top: 200px;
    font-weight: 800; font-size: 44px; line-height: 47px;
    color: var(--white); text-transform: uppercase; letter-spacing: 0.5px;
  }
  .headline .accent { color: var(--accent-blue); }
  .brand-badge {
    position: absolute; left: 378px; top: 300px;
    display: flex; align-items: center; gap: 8px;
  }
  .brand-badge .dot {
    width: 26px; height: 26px; border-radius: 50%;
    background: var(--white);
  }
  .brand-badge .name {
    font-weight: 600; font-size: 18px; color: var(--white); letter-spacing: 1px;
  }
  .intro {
    position: absolute; left: 38px; top: 418px; width: 468px;
    font-size: 10.6px; line-height: 17px; color: var(--text-soft);
  }
  .gallery {
    position: absolute; left: 24px; top: 550px;
    display: flex; gap: 12px;
  }
  .gallery .shot { width: 156px; height: 108px; }
  .shot-chapel { background: radial-gradient(ellipse at 60% 45%, #c9aa78 0%, #7a5e3e 55%, #3f3024 100%); }
  .shot-panel  { background: radial-gradient(ellipse at 40% 50%, #2a56b0 0%, #1a3a82 55%, #102a60 100%); }
  .shot-speaker { background: radial-gradient(ellipse at 65% 50%, #d4cbbb 0%, #a89a84 55%, #6a5842 100%); }
  .footer {
    position: absolute; left: 0; top: 680px; width: 540px; height: 84px;
    display: flex;
  }
  .footer .brand-block {
    width: 176px; background: var(--accent-blue);
    display: flex; align-items: center; justify-content: center;
    font-weight: 500; font-size: 20px; letter-spacing: 1.5px; color: var(--white);
  }
  .footer .contact {
    flex: 1; background: var(--navy-footer);
    display: flex; gap: 16px; padding: 16px 14px 0 18px;
    font-weight: 500; font-size: 10.5px; line-height: 19px; color: var(--white);
    white-space: nowrap;
  }
  .contact .address { font-style: normal; }
  .contact .reach { padding-top: 6px; }
  .contact .web { padding-top: 30px; }
</style>
</head>
<body>
  <main class="flyer">
    <div class="hero-photo" role="img" aria-label="Foto: beleuchtetes Kirchenschiff mit Bankreihen und Leuchtern"></div>

    <h1 class="headline">Benötigen<br>Sie <span class="accent">Audio &amp;</span><br><span class="accent">Visual</span> für<br>Ihre Kirche?</h1>

    <div class="brand-badge">
      <span class="dot"></span>
      <span class="name">ALPENTON</span>
    </div>

    <p class="intro">Unser zuverlässiges, engagiertes Team setzt Ihre Wünsche in den Bereichen Konzerte und Shows, audiovisuelle Installationen und smarten Gebäudeautomationen sowie Corporate Events von A bis Z um. Mit unserem grossen Netzwerk, der persönlichen Vertrautheit mit den regionalen Infrastrukturen und unserem hochwertigen technischen Equipment setzen wir Ihre Veranstaltung oder Ihre Festinstallation perfekt in Szene. Wir denken an alles und an jedes Detail. Als Kundin oder Kunde erhalten Sie ein individuell abgestimmtes Gesamtkonzept.</p>

    <div class="gallery">
      <div class="shot shot-chapel" role="img" aria-label="Foto: Kircheninnenraum mit Kreuz und Bankreihen"></div>
      <div class="shot shot-panel" role="img" aria-label="Bildschirmansicht: Bedienoberfläche mit Mikrofon- und Medienreglern"></div>
      <div class="shot shot-speaker" role="img" aria-label="Foto: Lautsprecher neben Altar mit Blumen"></div>
    </div>

    <footer class="footer">
      <div class="brand-block">ALPENTON</div>
      <div class="contact">
        <address class="address">Talweg 14<br>6300 Musterdorf</address>
        <div class="reach">041 555 01 23<br>mail@alpen-ton.ch</div>
        <div class="web">www.alpen-ton.ch</div>
      </div>
    </footer>
  </main>
</body>
</html>
```